Logo and packaging design for a food brand: Noble Drippings

Dear designer,

I'm located in Vancouver, British Columbia, Canada, and I'm launching a brand of products made of beef tallow. It's called Noble Drippings. I'm ultimately looking for a designer that can help me build the brand and create a series of products.

Here is what I need at this point:

- A logo for Noble Drippings (playing with the letters N and D - sketch using SketchMind attached)
- A packaging design for the PREMIUM WAGYU TALLOW - 235 ml (= 8 oz: https://www.vessora-supply.example/item/JX-40211/glass-jar-8-oz-black-cap)
- Glass jar with a label all around it and a lid seal label
- Primary colours: black, white, gold
- Secondary colours if needed: Canada red and light grey
- Fonts: not specified, looking forward to your inputs on what works
- Please refer to our #1 competitor as reference: https://www.harlowmeadowfoods.example/collections/items (we like their design style as well)
- #2 competitor to be used as reference: https://brisketbarn.example/items/1-jar-14-0-oz-organic-grass-fed-beef-tallow

- Information for the packaging:
PREMIUM WAGYU BEEF TALLOW
100% PURE
(optional) PRODUCED IN CANADA
NUTRITIONAL VALUE (we don't have the numbers yet, but please create a placeholder/mockup for this section)
* You can also add more information following the example from our Competitor 01

- Please feel free to improve the logo, but keep the concept of Noble Drippings (or ND) + the face of a bull
- Finally, I'd also love to see two colour schemes: one dark and one bright - I hope it's not asking too much

Target Market(s)

North America

Industry/Entity Type

Food

Font styles to use
Sans Serif
Script

Colors
FFC000
F8CF3A
FAE287
FDF2CF
FEFAEE

Requirements
Must have
• Incorporate gold, black and white
Nice to have
• Play with the letters ND in the logo (company name: Noble Drippings)
Should not have
• Many colours

```html
<!DOCTYPE html>
<html lang="en">
<head>
<meta charset="utf-8">
<title>Noble Drippings — Logo and Wagyu Tallow Label</title>
<link href="https://fonts.googleapis.com/css2?family=Saira+Condensed:wght@300&family=Poppins:wght@500;600;700;800&display=swap" rel="stylesheet">
<style>
  :root {
    --canvas: #f9f9f9;
    --ink: #000000;
    --paper: #ffffff;
    --gold: #d4ac0d;
  }
  * { margin: 0; padding: 0; box-sizing: border-box; }
  html, body { width: 1200px; height: 1200px; overflow: hidden; }
  body { background: var(--canvas); position: relative; font-family: "Poppins", sans-serif; }

  .brand-lockup { position: absolute; left: 110px; top: 140px; height: 230px; display: flex; align-items: center; gap: 30px; }
  .brand-lockup__mark { width: 226px; height: 226px; border: 6px solid var(--ink); border-radius: 50%; flex: none; }
  .brand-lockup__name { font-family: "Saira Condensed", sans-serif; font-weight: 300; font-size: 100px; line-height: 1; color: var(--ink); white-space: nowrap; }

  .label { position: absolute; left: 202px; top: 479px; width: 879px; height: 402px; border: 1px solid #cfcfcf; }
  .label__front { position: absolute; left: 0; top: 0; width: 427px; height: 100%; background: var(--paper); overflow: hidden; }
  .label__header { height: 128px; background: var(--ink); display: flex; align-items: center; padding-left: 26px; gap: 12px; }
  .label__header-mark { width: 84px; height: 84px; border: 3px solid var(--paper); border-radius: 50%; flex: none; }
  .label__header-name { font-family: "Saira Condensed", sans-serif; font-weight: 300; font-size: 36px; color: var(--paper); white-space: nowrap; }
  .label__product { position: absolute; left: 18px; top: 138px; font-weight: 800; font-size: 88px; line-height: 1; color: var(--ink); white-space: nowrap; }
  .label__band { position: absolute; left: 0; top: 232px; width: 427px; height: 60px; background: var(--gold); color: var(--paper); font-weight: 800; font-size: 54px; line-height: 62px; padding-left: 20px; white-space: nowrap; letter-spacing: -0.5px; }
  .label__ingredients-title { position: absolute; left: 22px; top: 317px; font-weight: 700; font-size: 21px; color: var(--gold); }
  .label__ingredients { position: absolute; left: 22px; top: 345px; font-weight: 600; font-size: 16px; color: var(--ink); }
  .label__weight { position: absolute; left: 0; top: 378px; width: 122px; height: 20px; background: var(--ink); color: var(--paper); font-weight: 600; font-size: 10.5px; line-height: 20px; padding-left: 22px; }
  .label__origin { position: absolute; right: 5px; top: 381px; font-weight: 500; font-size: 11px; color: var(--gold); }

  .label__back { position: absolute; left: 427px; top: 0; width: 452px; height: 100%; background: var(--ink); }
  .label__back svg { position: absolute; left: 0; top: 0; }
</style>
</head>
<body>
  <div class="brand-lockup">
    <div class="brand-lockup__mark" aria-hidden="true"></div>
    <div class="brand-lockup__name">Noble Drippings</div>
  </div>

  <div class="label">
    <div class="label__front">
      <div class="label__header">
        <div class="label__header-mark" aria-hidden="true"></div>
        <div class="label__header-name">Noble Drippings</div>
      </div>
      <div class="label__product">WAYGU</div>
      <div class="label__band">BEEF TALLOW</div>
      <div class="label__ingredients-title">INGREDIATES :</div>
      <div class="label__ingredients">Rendered Waygu Beef Fat</div>
      <div class="label__weight">NET WT 42 OZ</div>
      <div class="label__origin">Manufactured in Canada</div>
    </div>

    <div class="label__back">
      <svg width="452" height="402" viewBox="0 0 452 402" aria-label="Nutrition information placeholder" role="img">
        <g stroke="#ffffff" fill="none">
          <rect class="nutrition-frame" x="39.5" y="53.5" width="377" height="179" stroke-width="1"/>
          <g class="nutrition-lines" stroke-width="3">
            <line x1="48" y1="70" x2="407" y2="70"/>
            <line x1="48" y1="87" x2="407" y2="87"/>
            <line x1="48" y1="104" x2="407" y2="104"/>
            <line x1="48" y1="121" x2="407" y2="121"/>
            <line x1="48" y1="148" x2="407" y2="148"/>
            <line x1="48" y1="164" x2="407" y2="164"/>
            <line x1="48" y1="181" x2="407" y2="181"/>
            <line x1="48" y1="198" x2="407" y2="198"/>
          </g>
          <g class="detail-lines" stroke-width="3">
            <line x1="48" y1="258" x2="225" y2="258"/>
            <line x1="48" y1="275" x2="225" y2="275"/>
            <line x1="48" y1="292" x2="225" y2="292"/>
            <line x1="48" y1="309" x2="225" y2="309"/>
            <line x1="48" y1="326" x2="225" y2="326"/>
            <line x1="48" y1="343" x2="225" y2="343"/>
          </g>
        </g>
        <rect class="info-box" x="278" y="258" width="133" height="89" fill="#ffffff"/>
      </svg>
    </div>
  </div>
</body>
</html>
```